NEW Escape Room. Fun, Dark and Mysterious.

Escape Room Website. Bookings and scheduling of appointments will be organised with Bookvane through the site. Most appointments will be created online through the booking system with some payments coming through in person by drop-ins. Groups will be from 2 - 8 people with a sliding scale of prices. We will start with one game playable and one saying coming soon. We will also eventually have 4 games up and running at once so will need it to be able to expand. We don't have any images of the rooms because it all relies heavily on mystery. Appointments are each 1 hour long with 30 minutes in between.

Target Market(s)

15-35 year olds

Coding

Coded - Design and coding required

Number of Pages Required

5+ page

Font styles to use
Decorative

Colors

Designer to choose colors to be used in the design.

Requirements
Must have
• Graphics showing what an escape room is.
• Page for About - What is an escape room
• Page for Games - Showing each of the different games which can be played with links to booking page. We have one game to start - the surgeons shadows. A victorian doctors office and serial killers. Then a game coming soon which is aztec/mayan/jungle/harold Crane feel.
• FAQ Page
Nice to have
• Graphics for multiple players ie 2 players, 3 players, 4 players etc
• Dark and Mysterious feel.
• Inspiration from Puzzle Vault, Cipher Lodge, Quest Lockbox
Should not have
• Cartoony/childish. Pink.
• Not bloody or dripping letters etc - not cliche.
• Not horror themed.

```html
<!DOCTYPE html>
<html lang="en">
<head>
<meta charset="utf-8">
<title>Contact Us — The Locked Hour</title>
<link href="https://fonts.googleapis.com/css2?family=Cinzel:wght@400;700&family=Lato:wght@400;700;900&display=swap" rel="stylesheet">
<style>
  :root{
    --page:#1c1f1f;
    --panel:#0f1413;
    --black:#070808;
    --gold:#e39a0f;
    --white:#ffffff;
    --muted:#cfcfcf;
    --field:#e6e6e6;
    --field-text:#8a8a8a;
  }
  *{box-sizing:border-box;margin:0;padding:0}
  html,body{width:1200px;height:2560px;overflow:hidden;background:var(--page)}
  body{position:relative;font-family:"Lato",sans-serif;color:var(--white)}

  .hero{position:absolute;left:0;top:0;width:1200px;height:460px;
    background:linear-gradient(90deg,#050606 0%,#0b0d0d 45%,#20262a 75%,#0a0c0c 100%)}
  .hero-scene{position:absolute;left:560px;top:130px;width:640px;height:330px;
    background:radial-gradient(ellipse at 45% 75%,rgba(140,150,150,.35) 0%,rgba(40,46,48,.25) 40%,rgba(0,0,0,0) 75%)}
  .brand{position:absolute;left:130px;top:60px;display:flex;align-items:center;gap:10px;
    font-family:"Cinzel",serif;font-weight:700;font-size:20px;color:var(--gold)}
  .brand-dot{width:14px;height:14px;border-radius:50%;background:var(--gold)}
  .nav{position:absolute;top:64px;left:560px;display:flex;align-items:center;font-size:17px;font-weight:700}
  .nav a{color:var(--white);text-decoration:none;margin-right:44px}
  .nav a.current{color:var(--gold)}
  .btn-book{position:absolute;left:920px;top:56px;width:160px;height:52px;border:2px solid var(--gold);
    color:var(--white);font-size:16px;font-weight:700;display:flex;align-items:center;justify-content:center;letter-spacing:.5px}
  .hero-title{position:absolute;left:120px;top:262px;font-family:"Cinzel",serif;font-size:78px;font-weight:400;letter-spacing:1px}

  .map{position:absolute;left:124px;top:612px;width:556px;height:388px;
    background:linear-gradient(135deg,#d9e4cf 0%,#eef0e6 40%,#bcd3e6 75%,#9fc2e3 100%)}
  .info{position:absolute;left:688px;top:612px;width:384px;height:388px;background:var(--panel);
    display:flex;flex-direction:column;justify-content:center;align-items:center;text-align:center;gap:30px;font-size:16px;color:var(--muted)}

  .form-title{position:absolute;left:0;width:1200px;top:1114px;text-align:center;font-size:40px;font-weight:900;letter-spacing:1px}
  .field{position:absolute;background:var(--field);border-radius:3px;color:var(--field-text);font-size:14px;padding:16px 18px}
  .send{position:absolute;left:496px;top:1760px;width:204px;height:60px;background:var(--gold);
    display:flex;align-items:center;justify-content:center;font-weight:900;font-size:17px}

  .footer{position:absolute;left:0;top:2040px;width:1200px;height:520px;background:var(--black)}
  .footer-texture{position:absolute;left:0;bottom:0;width:1200px;height:240px;
    background:linear-gradient(180deg,rgba(7,8,8,1) 0%,#1a1b1b 55%,#2a2a2a 100%)}
  .footer-brand{position:absolute;left:0;top:40px;width:1200px;display:flex;justify-content:center;align-items:center;gap:12px;
    font-family:"Cinzel",serif;font-size:32px;font-weight:700;color:var(--gold)}
  .footer-brand .brand-dot{width:24px;height:24px}
  .footer-name{position:absolute;left:0;top:128px;width:1200px;text-align:center;font-family:"Cinzel",serif;font-size:26px}
  .footer-nav{position:absolute;top:224px;left:0;width:1200px;display:flex;justify-content:center;gap:40px;font-size:16px;font-weight:700}
  .social{position:absolute;top:300px;left:0;width:1200px;display:flex;justify-content:center;gap:40px}
  .social span{width:28px;height:28px;background:var(--white);border-radius:4px}
  .copyright{position:absolute;top:484px;left:0;width:1200px;text-align:center;font-size:13px;color:var(--muted)}
</style>
</head>
<body>
  <header class="hero">
    <div class="hero-scene" role="img" aria-label="Dim attic with a lone rocking chair in a shaft of light"></div>
    <div class="brand"><span class="brand-dot"></span>The Locked Hour</div>
    <nav class="nav">
      <a href="#">About</a><a href="#">Games</a><a class="current" href="#">Contact Us</a><a href="#">FAQ</a>
    </nav>
    <div class="btn-book">BOOK A GAME</div>
    <h1 class="hero-title">CONTACT US</h1>
  </header>

  <main>
    <div class="map" role="img" aria-label="Street map of Melbourne showing the venue location"></div>
    <div class="info">
      <p>+61 3 5550 1427</p>
      <p>hello@thelockedhour.example</p>
      <p>214 Lantern Lane, Richmond VIC 3121,<br>Australia</p>
    </div>

    <h2 class="form-title">SEND US A MESSAGE</h2>
    <div class="field" style="left:240px;top:1224px;width:348px;height:48px">First Name</div>
    <div class="field" style="left:612px;top:1224px;width:348px;height:48px">Last Name</div>
    <div class="field" style="left:240px;top:1308px;width:720px;height:48px">Email Address</div>
    <div class="field" style="left:240px;top:1388px;width:720px;height:292px">Enter Your Message Here</div>
    <div class="send">SEND</div>
  </main>

  <footer class="footer">
    <div class="footer-texture" role="img" aria-label="Dark grainy stone texture"></div>
    <div class="footer-brand"><span class="brand-dot"></span>The Locked Hour</div>
    <div class="footer-name">THE LOCKED HOUR</div>
    <nav class="footer-nav"><span>About</span><span>Games</span><span>Contact Us</span><span>FAQ</span></nav>
    <div class="social"><span></span><span></span><span></span></div>
    <p class="copyright">©2020 The Locked Hour. All Rights Reserved.</p>
  </footer>
</body>
</html>
```